Create new background graphics - aviation quoting portal

We need to update these backgrounds with the new logo and the Talvex KR72 Orbia Jet instead of the Morvana Quillon. Note there are two background files … feel free to change any of the design elements .. but the text box needs to stay in place … see file background image with software running file to complete the picture.

Target Market(s)

End users booking flights

Industry/Entity Type

Aviation

Requirements
Must have
• Cool picture of a Talvex KR72 Orbia jet in the background … instead of the Quillon 300 Jet. Must incorporate the new logo.
Nice to have
• Elements that suggest flight or speed and efficiency of travel. A powered by Brightmere Aviation Technologies tag.

```html
<!DOCTYPE html>
<html lang="en">
<head>
<meta charset="utf-8">
<title>Skyvault Quoting Portal</title>
<link href="https://fonts.googleapis.com/css2?family=Open+Sans:ital,wght@0,400;0,600;0,700;1,400&display=swap" rel="stylesheet">
<style>
  :root {
    --navy: #1d5a85;
    --label: #1f6391;
    --field-border: #1d5a85;
    --placeholder: #5f6670;
    --text: #1a1a1a;
    --header-band: #dfe5ee;
    --panel: #ffffff;
    --go-green: #7dc243;
    --logout-bg: #e3e7ef;
    --brand-light: #f2f6fb;
  }
  * { box-sizing: border-box; margin: 0; padding: 0; }
  html, body { width: 1200px; height: 800px; overflow: hidden; }
  body { font-family: "Open Sans", sans-serif; background: #1b2a4a; }

  .portal {
    position: relative; width: 1200px; height: 800px; overflow: hidden;
  }
  .hero-scene {
    position: absolute; inset: 0;
    background:
      radial-gradient(ellipse 520px 170px at 820px 520px, rgba(226,230,238,.85), rgba(200,205,215,.35) 55%, transparent 75%),
      radial-gradient(ellipse 700px 260px at 420px 440px, rgba(255,150,40,.9), transparent 70%),
      linear-gradient(180deg, #6b2130 0%, #b0362a 18%, #d9542a 35%, #f28a2c 48%, #c4522b 58%, #3d4a6a 72%, #7d9cc0 88%, #c9dcec 100%);
  }
  .hero-scene::after {
    content: ""; position: absolute; inset: 0;
    background: linear-gradient(100deg, transparent 55%, rgba(38,70,130,.55) 100%);
  }

  .quote-panel {
    position: absolute; left: 69px; top: 0; width: 453px; height: 525px;
    background: var(--panel); border-radius: 0 0 19px 19px; overflow: hidden;
    box-shadow: 0 4px 14px rgba(0,0,0,.25);
  }
  .panel-header {
    height: 96px; background: var(--header-band);
    display: flex; align-items: center; padding-left: 34px;
  }
  .brand-name {
    font-size: 40px; font-weight: 600; color: var(--navy); letter-spacing: 2px;
  }

  .trip-type { position: absolute; top: 112px; left: 33px; display: flex; gap: 30px; }
  .trip-option {
    display: flex; align-items: center; gap: 8px;
    font-size: 14px; font-weight: 600; color: var(--label);
  }
  .radio {
    width: 17px; height: 17px; border: 1.5px solid #555; border-radius: 50%;
    display: grid; place-items: center;
  }
  .radio.is-selected::after {
    content: ""; width: 10px; height: 10px; border-radius: 50%; background: var(--navy);
  }

  .field {
    position: absolute; height: 27px; border: 1.8px solid var(--field-border);
    border-radius: 14px; display: flex; align-items: center; overflow: hidden;
    background: #fff;
  }
  .field-icon {
    height: 100%; background: var(--navy); display: grid; place-items: center; flex: none;
  }
  .field-icon svg { display: block; }
  .field-text {
    flex: 1; padding-left: 8px; font-size: 13px; font-style: italic;
    color: var(--placeholder); white-space: nowrap;
  }
  .field-text.is-value { font-style: normal; color: var(--text); font-size: 13.5px; }
  .caret {
    width: 0; height: 0; border-left: 5.5px solid transparent; border-right: 5.5px solid transparent;
    border-top: 6px solid #555; margin-right: 14px;
  }
  .field.is-plain .field-text { padding-left: 16px; }

  .field-label {
    position: absolute; font-size: 13.5px; font-weight: 600; color: var(--label);
  }

  .btn-continue {
    position: absolute; left: 32px; top: 467px; width: 100px; height: 24px;
    background: var(--go-green); color: #fff; border-radius: 12px;
    font-size: 13.5px; font-weight: 700; display: grid; place-items: center;
  }
  .btn-logout {
    position: absolute; left: 152px; top: 467px; width: 183px; height: 24px;
    background: var(--logout-bg); border-radius: 12px; font-size: 13.5px;
    display: grid; place-items: center; color: var(--text);
  }
  .btn-logout em { font-style: italic; }
  .btn-logout strong { font-weight: 700; }
  .remember {
    position: absolute; left: 166px; top: 496px; font-size: 13px; font-style: italic;
    color: var(--text); display: flex; align-items: center; gap: 6px;
  }
  .checkbox { width: 10px; height: 10px; border: 1px solid #333; position: relative; }
  .checkbox::after {
    content: ""; position: absolute; left: 2px; top: 0; width: 3px; height: 6px;
    border: solid #333; border-width: 0 1.4px 1.4px 0; transform: rotate(40deg);
  }

  .powered-by {
    position: absolute; left: 898px; top: 678px; display: flex; align-items: center; gap: 12px;
    color: var(--brand-light); font-weight: 600;
  }
  .powered-by .mark {
    width: 76px; height: 76px; border-radius: 50%; border: 3px solid var(--brand-light);
  }
  .powered-by .name { line-height: 1; }
  .powered-by .name-main { display: block; font-size: 30px; letter-spacing: .5px; }
  .powered-by .name-sub { display: block; font-size: 11.5px; letter-spacing: 1.6px; margin-top: 6px; }
</style>
</head>
<body>
<main class="portal">
  <div class="hero-scene" role="img" aria-label="Talvex KR72 Orbia Jet parked on a wet runway under a fiery orange sunset sky"></div>

  <section class="quote-panel" aria-label="Flight quote request">
    <header class="panel-header"><span class="brand-name">SKYVAULT</span></header>

    <div class="trip-type">
      <label class="trip-option">One-way <span class="radio is-selected"></span></label>
      <label class="trip-option">Round-Trip <span class="radio"></span></label>
      <label class="trip-option">Multi-Leg <span class="radio"></span></label>
    </div>

    <div class="field" style="left:30px;top:144px;width:382px;">
      <span class="field-icon" style="width:44px;">
        <svg width="26" height="16" viewBox="0 0 26 16"><path d="M2 14 Q8 15 14 11" stroke="#fff" stroke-width="1.2" stroke-dasharray="1.5 2" fill="none"/><path d="M15 9 L24 2 L25 3.5 L18 10 Z M17 5 L21 6 L19 8 Z" fill="#fff"/></svg>
      </span>
      <span class="field-text">Enter Airport Code [KXXX], City, Address or Landmark</span>
    </div>
    <div class="field" style="left:30px;top:178px;width:382px;">
      <span class="field-icon" style="width:44px;">
        <svg width="26" height="16" viewBox="0 0 26 16"><path d="M2 3 L10 10 L9 11.5 L1 5 Z M4 8 L7 5 L8 7 Z" fill="#fff"/><path d="M11 12 Q17 15 24 13" stroke="#fff" stroke-width="1.2" stroke-dasharray="1.5 2" fill="none"/></svg>
      </span>
      <span class="field-text">Enter Airport Code [KXXX], City, Address or Landmark</span>
    </div>

    <span class="field-label" style="left:37px;top:228px;">Departure Date/Time</span>
    <span class="field-label" style="left:236px;top:228px;">Departure Time Flexibility</span>

    <div class="field" style="left:30px;top:251px;width:170px;">
      <span class="field-icon" style="width:31px;">
        <svg width="15" height="15" viewBox="0 0 15 15"><rect x="1" y="2.5" width="13" height="11" fill="none" stroke="#fff" stroke-width="1.2"/><line x1="1" y1="5.5" x2="14" y2="5.5" stroke="#fff"/><line x1="4.5" y1="1" x2="4.5" y2="4" stroke="#fff"/><line x1="10.5" y1="1" x2="10.5" y2="4" stroke="#fff"/></svg>
      </span>
      <span class="field-text is-value">2/16/2020&nbsp; 9:00 AM</span>
    </div>
    <div class="field" style="left:229px;top:251px;width:183px;">
      <span class="field-icon" style="width:31px;">
        <svg width="16" height="16" viewBox="0 0 16 16"><circle cx="8" cy="8" r="6.5" fill="none" stroke="#fff" stroke-width="1.3"/><path d="M8 4 V8 L5.5 10" stroke="#fff" stroke-width="1.3" fill="none"/></svg>
      </span>
      <span class="field-text">Flex From</span>
      <span class="caret"></span>
    </div>

    <span class="field-label" style="left:37px;top:293px;">Passengers</span>
    <div class="field" style="left:30px;top:316px;width:170px;">
      <span class="field-icon" style="width:31px;">
        <svg width="14" height="16" viewBox="0 0 14 16"><circle cx="7" cy="4.5" r="3" fill="none" stroke="#fff" stroke-width="1.3"/><path d="M1.5 15 V11 Q1.5 8.5 4.5 8.5 H9.5 Q12.5 8.5 12.5 11 V15 Z" fill="none" stroke="#fff" stroke-width="1.3"/></svg>
      </span>
      <span class="field-text">Total Passengers</span>
      <span class="caret" style="margin-right:16px;"></span>
    </div>

    <span class="field-label" style="left:37px;top:357px;">Options</span>
    <div class="field is-plain" style="left:31px;top:380px;width:381px;">
      <span class="field-text">Optional Aircraft types to Include</span>
      <span class="caret"></span>
    </div>
    <div class="field is-plain" style="left:31px;top:412px;width:381px;">
      <span class="field-text">Optional Certificates</span>
      <span class="caret"></span>
    </div>

    <span class="btn-continue">Continue</span>
    <span class="btn-logout"><span><em>Member/Broker</em> <strong>Logout</strong></span></span>
    <span class="remember"><span class="checkbox"></span>Remember Me</span>
  </section>

  <aside class="powered-by">
    <span class="mark"></span>
    <span class="name"><span class="name-main">BRIGHTMERE</span><span class="name-sub">AVIATION TECHNOLOGIES</span></span>
  </aside>
</main>
</body>
</html>
```